WordPress design for BraxtonVell.com

*****
OVERVIEW
*****
BraxtonVell.com needs a fresh, clean, professional design that effectively illustrates its talent in a thoughtful, impressive, and impactful way.
Vell Architecture & Interiors (www.braxtonvell.com) is a well-established, prestigious, well-publicized New England USA architecture firm. Founded in 1996, the privately-held company specializes in high-end residential projects with a focus on classic New England style architecture.
Business contact information is as noted below:
Address:
Vell Architecture & Interiors
87 Orchard Terrace
Needham, MA 02817
Telephone:
617-555-0138
781-555-0274
Email:
info@braxtonvell.com
An excerpt from the current site describes the outfit with this:
"Our architecture and interior design practices are centered around the philosophy that successful living spaces combine a focus on richly articulated detail and an in-depth knowledge of quality construction techniques."
*****
DESIGN RESEARCH
*****
In reviewing design ideas, the following sites were appealing:
Good
- Marcus Thorne Architects (http://mtaarchitects-example.com/) - Simple and clean, but almost too simple.
Better
- Penrose Galt Architecture (http://www.penrosegalt-example.com/) - Direct portfolio access. Simple and clean.
Best
- Brimwell Architects (http://www.brimwellarchitects-example.com/) - Clean, simple, easy to navigate
- QRV Architecture & Interiors (http://www.qrv-architects-example.com/) - Excellent use of high-resolution media, transitions, and navigation.
Here is an example of what is NOT desired:
Tolland Pryce Architects (http://www.tollandpryce-example.com/) - Cluttered, tight landing page. Uncertain navigation.
*****
OTHER DETAILS
*****
The grey in the Vell Architecture & Interiors logo is hex 636363. The font is unknown.
Updates
Project Deadline Extended
Reason: Hello everyone,
Thank you for your continued patience with this project. As it turns out, a critical member of the decision making team on our client's end has been out of the office this week. She will be back next week and is ready to be fully engaged with this. That said, we are extending the contest for at least 5 days. Next week will be much more active.
Thank you for your understanding.
Glasswick Technology Services
Project Deadline Extended
Reason: Hello everyone,
The customer was on vacation and only returned Monday of this week. That said, we need to extend the deadline for 5 days to afford time for review and comment.
Thank you for your patience! The designs submitted thus far are fantastic!
Thanks again,
Project Deadline Extended
Reason: Hello,
With so many designs, the customer is taking longer than anticipated to review them. They are looking at them offline and will process a large batch of comments when ready.
That said, the contest is being extended again.
Thank you for your continued patience.
Project Deadline Extended
Reason: Hello,
Because there are 108 designs to review and comment on, this is taking much longer than anticipated. That said, the contest is being extended another 5 days to ensure the customer has the desired outcome.
Thank you,
Target Market(s)
- Would-be clients
- Landowners
- Construction firms and general contractors
- High-end residential component manufacturers
- Media outlets
- All others interested in high-end residential architecture and interior design
Industry/Entity Type
Architecture
Requirements
Must have
- - Lots of media capabilities, such as embedded video (via ClipStream is fine), project image gallery, sliders for various functions, and social media integrations
- - At least one large slider on the landing page is critical, as well as space for standard lead-in things, such as news/events, opportunities, project highlights, and the likes
- - A high-resolution project showcase - finished projects and works in progress - is critical
- - A place to highlight business partners with the potential for reciprocation
- Form capabilities for things like information requests and general contacts from the public
- - Design must be handed off in a logically-layered (for WordPress) PSD with any and all additional source files provided (e.g. Photoshop, Illustrator, fonts, etc)
Nice to have
- - The WordPress design should be capable of fitting into the very popular FernLayouts Trellis theme.

```html
<!DOCTYPE html>
<html lang="en">
<head>
<meta charset="utf-8">
<title>Vell Architecture &amp; Interiors</title>
<link href="https://fonts.googleapis.com/css2?family=Cormorant+Garamond:wght@500;600&family=Oswald:wght@400;500;600&family=Open+Sans:wght@400;600;700&display=swap" rel="stylesheet">
<style>
:root{
  --teal:#17a99b;
  --teal-dark:#0f8a7e;
  --teal-pale:#e6f3f1;
  --grey:#636363;
  --ink:#333333;
  --muted:#8a8a8a;
  --line:#d9d9d9;
  --footer:#2c2c2c;
  --footer-deep:#222222;
  --white:#ffffff;
}
*{box-sizing:border-box;margin:0;padding:0}
html,body{width:1200px;height:2636px;overflow:hidden;background:var(--white)}
body{font-family:"Open Sans",Arial,sans-serif;color:var(--ink);position:relative}
a{color:inherit;text-decoration:none}

/* header */
.site-header{height:140px;position:relative}
.brand{position:absolute;left:100px;top:26px}
.brand-name{font-family:"Cormorant Garamond",Georgia,serif;font-weight:600;font-size:60px;letter-spacing:3px;color:var(--teal);line-height:1}
.brand-tag{font-size:11px;letter-spacing:3px;color:var(--grey);margin-top:6px;text-transform:uppercase}
.header-meta{position:absolute;right:100px;top:22px;font-size:12px;color:var(--muted);display:flex;gap:18px}
.header-meta .phone{color:var(--teal);font-weight:700}
.search{position:absolute;right:100px;top:56px;display:flex}
.search-field{width:260px;height:36px;border:1px solid var(--line);font-size:12px;color:var(--muted);padding:9px 12px}
.search-btn{width:36px;height:36px;background:#444;display:flex;align-items:center;justify-content:center}

/* nav */
.main-nav{height:44px;background:var(--teal);display:flex;padding-left:100px}
.main-nav a{color:var(--white);font-size:11px;font-weight:700;text-transform:uppercase;letter-spacing:.5px;padding:0 13px;line-height:44px}
.main-nav a.active{background:var(--teal-dark)}

/* hero */
.hero{position:relative;height:556px;background:linear-gradient(180deg,#8fa3ae 0%,#b7c2c4 30%,#7d7a70 55%,#4f5a44 80%,#3a4535 100%);box-shadow:0 10px 18px rgba(0,0,0,.25);z-index:1}
.hero::after{content:"";position:absolute;inset:0;background:rgba(0,0,0,.28)}
.hero-content{position:absolute;z-index:2;left:0;right:0;top:190px;text-align:center;color:var(--white)}
.play{width:86px;height:86px;border:3px solid rgba(255,255,255,.85);border-radius:50%;margin:0 auto 18px;display:flex;align-items:center;justify-content:center}
.hero-title{font-family:"Oswald",Arial,sans-serif;font-weight:600;font-size:34px;line-height:44px;text-transform:uppercase;letter-spacing:.5px}
.hero-text{width:620px;margin:14px auto 0;font-size:12px;line-height:20px;color:#eaeaea}
.hero-down{position:absolute;z-index:2;left:578px;bottom:16px;width:44px;height:44px;border-radius:50%;background:rgba(0,0,0,.45);display:flex;align-items:center;justify-content:center}
.hero-arrow{position:absolute;z-index:2;top:240px;width:40px;height:40px;border:2px solid rgba(255,255,255,.8);border-radius:50%;display:flex;align-items:center;justify-content:center}
.hero-arrow.prev{left:50px}.hero-arrow.next{right:50px}

/* section heading */
.section-title{text-align:center}
.section-title h2{font-family:"Oswald",Arial,sans-serif;font-weight:500;font-size:22px;line-height:30px;letter-spacing:1px;text-transform:uppercase;color:var(--ink)}
.divider{display:flex;align-items:center;justify-content:center;gap:10px;margin-top:10px}
.divider span{width:150px;height:1px;background:var(--teal)}
.divider i{width:14px;height:14px;border:1px solid var(--teal);border-radius:50%;display:block}

/* projects */
.projects{height:818px;padding-top:80px}
.gallery{width:1000px;margin:34px auto 0}
.feature{position:relative;height:360px;background:linear-gradient(120deg,#5f6e5c 0%,#8d9f9c 35%,#dfe3e2 60%,#c9c4b7 80%,#6b7860 100%)}
.feature-copy{position:absolute;left:40px;top:40px;width:440px;color:var(--white)}
.feature-copy h3{font-family:"Oswald",Arial,sans-serif;font-weight:500;font-size:17px;letter-spacing:.5px;text-transform:uppercase}
.feature-copy p{font-size:11px;line-height:18px;margin-top:12px;color:#f0f0f0}
.btn-more{display:inline-block;margin-top:18px;border:1px solid var(--white);color:var(--white);font-size:11px;padding:6px 14px}
.tiles{display:flex;gap:10px;margin-top:10px}
.tile{height:250px;flex:1}
.tile.kitchen{background:linear-gradient(135deg,#e9e9e6 0%,#bdbcb6 45%,#4a4a48 100%)}
.tile.bedroom{background:linear-gradient(90deg,#8aa14f 0%,#7b8a3e 35%,#6a3a2a 60%,#d9d0c0 100%)}

/* news */
.news{height:400px;background:var(--teal-pale);position:relative;padding-top:28px}
.news-arrows{position:absolute;right:100px;top:118px;display:flex;gap:4px}
.news-arrows b{width:26px;height:22px;background:#cfd8d6;display:flex;align-items:center;justify-content:center}
.news-cols{width:1000px;margin:62px auto 0;display:flex}
.news-item{flex:1;padding-right:40px}
.news-item + .news-item{border-left:1px solid var(--line);padding-left:40px;padding-right:0}
.news-item h4{font-family:"Oswald",Arial,sans-serif;font-weight:500;font-size:16px;text-transform:uppercase;letter-spacing:.5px}
.news-date{font-size:10px;color:var(--teal);margin-top:6px;font-weight:600}
.news-item p{font-size:11px;line-height:19px;color:#666;margin-top:10px}
.read-more{font-size:10px;font-weight:700;color:var(--teal);text-transform:uppercase;white-space:nowrap}

/* showcase */
.showcase{height:362px;padding-top:50px;position:relative}
.show-row{width:1000px;margin:28px auto 0;display:flex;gap:13px}
.shot{flex:1;height:170px}
.shot.s1{background:linear-gradient(180deg,#9fb8cf 0%,#e8e6e0 50%,#556b45 100%)}
.shot.s2{background:linear-gradient(180deg,#a9c7e3 0%,#f1ede6 55%,#c8b89c 100%)}
.shot.s3{background:linear-gradient(135deg,#d7d2c8 0%,#f3f0ea 50%,#8d8a80 100%)}
.shot.s4{background:linear-gradient(180deg,#f4f6f8 0%,#dfe6ec 50%,#a7b3bb 100%)}
.show-arrow{position:absolute;top:192px;width:30px;height:50px;display:flex;align-items:center;justify-content:center}
.show-arrow.prev{left:60px}.show-arrow.next{right:60px}

/* footer */
.site-footer{position:relative;height:316px;background:var(--footer);color:#bdbdbd}
.footer-cols{display:flex;padding:36px 100px 0;gap:40px}
.footer-col h5{font-family:"Oswald",Arial,sans-serif;font-weight:500;font-size:15px;color:var(--white);text-transform:uppercase;letter-spacing:.5px;margin-bottom:16px}
.footer-col li{list-style:none;font-size:11px;line-height:19px}
.col-links{width:200px}.col-contact{width:230px}.col-news{width:300px}.col-follow{flex:1;padding-left:40px}
.footer-col p{font-size:11px;line-height:18px}
.field{width:200px;height:26px;background:var(--white);margin-top:8px;font-size:10px;color:var(--muted);padding:6px 8px}
.subscribe{display:inline-block;margin-top:10px;background:var(--teal);color:var(--white);font-size:10px;font-weight:700;padding:7px 14px}
.social li{display:flex;align-items:center;gap:8px}
.social i{width:10px;height:10px;background:var(--teal);display:block}
.footer-bar{position:absolute;left:0;bottom:0;width:100%;height:36px;background:var(--footer-deep);display:flex;justify-content:space-between;align-items:center;padding:0 100px;font-size:10px;color:#9a9a9a}
</style>
</head>
<body>

<header class="site-header">
  <div class="brand">
    <div class="brand-name">VELL</div>
    <div class="brand-tag">Architecture &amp; Interiors</div>
  </div>
  <div class="header-meta">
    <span>Call us at: <span class="phone">617-555-0138</span></span>
    <span>login / register</span>
  </div>
  <div class="search">
    <div class="search-field">Search</div>
    <div class="search-btn"><svg width="14" height="14" viewBox="0 0 14 14"><circle cx="6" cy="6" r="4.5" fill="none" stroke="#fff" stroke-width="1.6"/><line x1="9.3" y1="9.3" x2="13" y2="13" stroke="#fff" stroke-width="1.6"/></svg></div>
  </div>
</header>

<nav class="main-nav">
  <a class="active" href="#">Home</a>
  <a href="#">About</a>
  <a href="#">Architecture</a>
  <a href="#">Interior Design</a>
  <a href="#">Works in Progress</a>
  <a href="#">Renovations and Additions</a>
  <a href="#">Recognition</a>
  <a href="#">Affiliates</a>
  <a href="#">Contact</a>
</nav>

<section class="hero" role="img" aria-label="Large white New England residence at dusk with lit windows and landscaped lawn">
  <div class="hero-arrow prev"><svg width="12" height="14" viewBox="0 0 12 14"><polyline points="9,1 3,7 9,13" fill="none" stroke="#fff" stroke-width="2"/></svg></div>
  <div class="hero-arrow next"><svg width="12" height="14" viewBox="0 0 12 14"><polyline points="3,1 9,7 3,13" fill="none" stroke="#fff" stroke-width="2"/></svg></div>
  <div class="hero-content">
    <div class="play"><svg width="28" height="32" viewBox="0 0 28 32"><polygon points="4,2 26,16 4,30" fill="#fff" opacity=".9"/></svg></div>
    <h1 class="hero-title">We provide homes flats and<br>estates for every wallet</h1>
    <p class="hero-text">Vell Architecture &amp; Interiors shapes classic New England homes with richly articulated detail, honest materials and quality construction. From coastal cottages to country estates, every project begins with listening and ends with a place that feels made for the people who live there.</p>
  </div>
  <div class="hero-down"><svg width="16" height="10" viewBox="0 0 16 10"><polyline points="1,1 8,8 15,1" fill="none" stroke="#fff" stroke-width="2"/></svg></div>
</section>

<section class="projects">
  <div class="section-title">
    <h2>Our Company Project</h2>
    <div class="divider"><span></span><i></i><span></span></div>
  </div>
  <div class="gallery">
    <div class="feature" role="img" aria-label="Modern white villa with palm trees and an open terrace">
      <div class="feature-copy">
        <h3>Dolore magna aliqua. Ut enim ad minim veniam</h3>
        <p>Lorem ipsum dolor sit amet, consectetur adipisicing elit, sed do eiusmod tempor incididunt ut labore et dolore magna aliqua. Ut enim ad minim veniam, quis nostrud exercitation ullamco laboris nisi ut aliquip ex ea commodo consequat. Duis aute irure dolor in reprehenderit in voluptate velit esse cillum dolore eu fugiat nulla pariatur.</p>
        <a class="btn-more" href="#">Read more</a>
      </div>
    </div>
    <div class="tiles">
      <div class="tile kitchen" role="img" aria-label="Bright open kitchen with white cabinets and pendant lights"></div>
      <div class="tile bedroom" role="img" aria-label="Bedroom with green feature wall and dark wood bed"></div>
    </div>
  </div>
</section>

<section class="news">
  <div class="section-title">
    <h2>Latest News / Events</h2>
    <div class="divider"><span></span><i></i><span></span></div>
  </div>
  <div class="news-arrows">
    <b><svg width="8" height="10" viewBox="0 0 8 10"><polyline points="6,1 2,5 6,9" fill="none" stroke="#fff" stroke-width="1.6"/></svg></b>
    <b><svg width="8" height="10" viewBox="0 0 8 10"><polyline points="2,1 6,5 2,9" fill="none" stroke="#fff" stroke-width="1.6"/></svg></b>
  </div>
  <div class="news-cols">
    <article class="news-item">
      <h4>Independent Senior Living</h4>
      <div class="news-date">AUGUST 06, 2016</div>
      <p>Our team completed a light-filled senior residence in Wellesley, pairing single-level living with generous porches, wide halls and warm natural finishes. The design keeps the quiet character of a classic shingle-style home while meeting every accessibility need. <a class="read-more" href="#">Read more</a></p>
    </article>
    <article class="news-item">
      <h4>Residential Care Homes</h4>
      <div class="news-date">AUGUST 06, 2016</div>
      <p>Join us this spring for an open studio evening on residential care homes. We will share plans, material samples and lessons learned from recent projects that bring comfort, dignity and New England craftsmanship to assisted living. <a class="read-more" href="#">Read more</a></p>
    </article>
  </div>
</section>

<section class="showcase">
  <div class="section-title">
    <h2>Project Showcase</h2>
    <div class="divider"><span></span><i></i><span></span></div>
  </div>
  <div class="show-arrow prev"><svg width="14" height="30" viewBox="0 0 14 30"><polyline points="12,2 2,15 12,28" fill="none" stroke="#bbb" stroke-width="2"/></svg></div>
  <div class="show-arrow next"><svg width="14" height="30" viewBox="0 0 14 30"><polyline points="2,2 12,15 2,28" fill="none" stroke="#bbb" stroke-width="2"/></svg></div>
  <div class="show-row">
    <div class="shot s1" role="img" aria-label="Colonial house entrance with white portico"></div>
    <div class="shot s2" role="img" aria-label="Shingle-style home exterior under blue sky"></div>
    <div class="shot s3" role="img" aria-label="Neutral toned living room interior"></div>
    <div class="shot s4" role="img" aria-label="Bright white kitchen and dining space"></div>
  </div>
</section>

<footer class="site-footer">
  <div class="footer-cols">
    <div class="footer-col col-links">
      <h5>Vell Studio</h5>
      <ul>
        <li>Home</li><li>About</li><li>Architecture</li><li>Interior Design</li>
        <li>Works in Progress</li><li>Renovations And Additions</li><li>Recognition / Affiliates</li>
      </ul>
    </div>
    <div class="footer-col col-contact">
      <h5>Contact Us</h5>
      <ul>
        <li>87 Orchard Terrace</li><li>Needham, MA 02817</li><li>info@braxtonvell.com</li>
        <li>617-555-0138</li><li>781-555-0274</li>
      </ul>
    </div>
    <div class="footer-col col-news">
      <h5>Sign to Newsletter</h5>
      <p>Get our latest projects, news and event invitations delivered straight to your inbox each month.</p>
      <div class="field">Name</div>
      <div class="field">Email</div>
      <a class="subscribe" href="#">SUBSCRIBE</a>
    </div>
    <div class="footer-col col-follow">
      <h5>Follow Us</h5>
      <ul class="social">
        <li><i></i>FaceLeaf</li><li><i></i>Chirpline</li><li><i></i>ClipStream</li><li><i></i>Snapgrid</li>
      </ul>
    </div>
  </div>
  <div class="footer-bar">
    <span>© 2016 - 2017 BraxtonVell.com. All rights reserved.</span>
    <span>↑ TOP</span>
  </div>
</footer>

</body>
</html>
```